Sleek business card design for digital agency.

Brief document attached for detailed description and inspiration. Looking for a minimalist sleek, cool, modern business card design.

Industry/Entity Type

Digital

```html
<!DOCTYPE html>
<html lang="en">
<head>
<meta charset="utf-8">
<title>Kestrel Labs — Business Card</title>
<link rel="stylesheet" href="https://fonts.googleapis.com/css2?family=Didact+Gothic&family=Open+Sans:wght@400;700&display=swap">
<style>
  :root {
    --stage-light: #f4f4f4;
    --stage-mid: #b9b9b9;
    --stage-dark: #6e6e6e;
    --card-black: #000000;
    --ink-white: #ffffff;
    --accent-blue: #00a9ec;
    --accent-blue-deep: #0093d4;
  }
  * { margin: 0; padding: 0; box-sizing: border-box; }
  html, body { width: 1200px; height: 1160px; overflow: hidden; }
  body {
    position: relative;
    font-family: "Open Sans", sans-serif;
    background: radial-gradient(ellipse 55% 60% at 50% 50%, var(--stage-light) 0%, var(--stage-mid) 55%, var(--stage-dark) 100%);
  }
  .card {
    position: absolute;
    top: 176px;
    width: 471px;
    height: 808px;
    background: var(--card-black);
    color: var(--ink-white);
    overflow: hidden;
  }
  .card--front { left: 92px; }
  .card--back { left: 636px; }

  .headline {
    position: absolute;
    top: 16px;
    right: 23px;
    text-align: right;
    font-weight: 700;
    font-size: 46px;
    line-height: 54px;
    letter-spacing: 0.3px;
  }
  .brand-mark {
    position: absolute;
    left: 24px;
    bottom: 18px;
    display: flex;
    align-items: center;
    gap: 10px;
    font-size: 26px;
    font-weight: 700;
  }
  .brand-mark__dot {
    width: 22px;
    height: 22px;
    border-radius: 50%;
    background: var(--accent-blue);
  }

  .monogram {
    position: absolute;
    left: 30px;
    top: 70px;
    font-size: 34px;
    font-weight: 700;
  }
  .corner-art {
    position: absolute;
    top: 0;
    right: 0;
    width: 196px;
    height: 310px;
    background: linear-gradient(160deg, var(--accent-blue) 0%, var(--accent-blue-deep) 100%);
  }
  .contact {
    position: absolute;
    left: 18px;
    top: 475px;
    font-family: "Didact Gothic", sans-serif;
    font-weight: 400;
  }
  .contact__name { font-size: 27px; line-height: 34px; }
  .contact__line { font-size: 21px; line-height: 28.2px; }
  .contact__gap { height: 28.2px; }
</style>
</head>
<body>
  <section class="card card--front">
    <h1 class="headline">KESTREL<br>MARKETING<br>SHRIMP</h1>
    <div class="brand-mark"><span class="brand-mark__dot"></span><span>Kestrel Labs</span></div>
  </section>

  <section class="card card--back">
    <div class="monogram">Kestrel Labs</div>
    <div class="corner-art" role="img" aria-label="Blue shrimp illustration emerging from the top right corner"></div>
    <div class="contact">
      <p class="contact__name">Daniel Hollis</p>
      <p class="contact__line">Marketing Director</p>
      <p class="contact__line">Drink order: G&amp;T with cucumber</p>
      <div class="contact__gap"></div>
      <p class="contact__line">Level 2, 18 Tamsin St</p>
      <p class="contact__line">East Marlow NSW 2999</p>
      <p class="contact__line">0400 000 123</p>
      <p class="contact__line">02 9000 0000</p>
      <p class="contact__line">dhollis@kestrellabs.com</p>
      <p class="contact__line">@dhollis81</p>
      <p class="contact__line">facebook.com/KestrelLabs</p>
    </div>
  </section>
</body>
</html>
```